Need a book cover design for a Lumora Book on Herbal Remedies

I need a book cover for my new ebook, here are the details:
Title: Meadow Cures
Sub-Heading: Buried Ancient Garden Tonics
Reclaiming the Wisdom of Roots for Everyday Wellness and Strength
Author: Nora Belcourt

```html
<!DOCTYPE html>
<html lang="en">
<head>
<meta charset="utf-8">
<title>Meadow Cures — Nora Belcourt</title>
<link rel="stylesheet" href="https://fonts.googleapis.com/css2?family=Tinos:wght@400;700&family=Arimo:wght@400&display=swap">
<style>
  :root {
    --ink-green: #0a7236;
    --bg-light: #e7f6ec;
    --bg-mint: #d3ece8;
    --bg-shade: #b9d6d0;
    --art-top: #5f9a4a;
    --art-mid: #4f8a42;
    --art-low: #2f6a44;
  }
  * { margin: 0; padding: 0; box-sizing: border-box; }
  html, body { width: 750px; height: 1200px; overflow: hidden; }
  body { background: var(--bg-light); }
  .cover {
    position: relative;
    width: 750px;
    height: 1200px;
    overflow: hidden;
    background:
      radial-gradient(ellipse 260px 520px at 430px 760px, var(--bg-shade) 0%, rgba(185,214,208,0) 70%),
      linear-gradient(160deg, var(--bg-light) 0%, #e1f3ec 45%, var(--bg-mint) 100%);
  }
  .title {
    position: absolute;
    left: 0;
    width: 750px;
    text-align: center;
    font-family: "Tinos", "Times New Roman", serif;
    font-weight: 400;
    font-size: 152px;
    line-height: 1;
    color: var(--ink-green);
  }
  .title-line-1 { top: 36px; }
  .title-line-2 { top: 155px; }
  .subtitle {
    position: absolute;
    top: 318px;
    left: 40px;
    width: 670px;
    text-align: center;
    font-family: "Arimo", Arial, sans-serif;
    font-size: 23px;
    line-height: 31px;
    letter-spacing: 0.4px;
    color: var(--ink-green);
  }
  .cover-art {
    position: absolute;
    left: 240px;
    top: 421px;
    width: 274px;
    height: 650px;
    background: linear-gradient(180deg, var(--art-top) 0%, var(--art-mid) 55%, var(--art-low) 100%);
  }
  .author {
    position: absolute;
    top: 1108px;
    left: 0;
    width: 750px;
    text-align: center;
    font-family: "Tinos", "Times New Roman", serif;
    font-weight: 700;
    font-size: 38px;
    letter-spacing: 13px;
    text-indent: 13px;
    color: var(--ink-green);
  }
</style>
</head>
<body>
  <main class="cover">
    <h1>
      <span class="title title-line-1">MEADOW</span>
      <span class="title title-line-2">CURES</span>
    </h1>
    <p class="subtitle">Buried Ancient Garden Tonics Reclaiming the Wisdom of Roots for Everyday Wellness and Strength</p>

    <div class="cover-art" role="img" aria-label="Illustration of a clear medicine capsule filled with moss, ferns and green herbs"></div>

    <p class="author">NORA BELCOURT</p>
  </main>
</body>
</html>
```